Bramwell Business Cards

Logo files are included. Full "Bramwell" logo should be included on the back of the business card. The B symbol should be included on the front with the contact information.

Bramwell, LLC is the company name and we do commercial construction and real estate development consulting services. Look for a fairly simple card design utilizing our logo.

```html
<!DOCTYPE html>
<html lang="en">
<head>
<meta charset="utf-8">
<title>Bramwell Business Cards</title>
<link rel="stylesheet" href="https://fonts.googleapis.com/css2?family=Montserrat:wght@400;500;600&display=swap">
<style>
  :root {
    --navy: #1b3549;
    --navy-soft: #21405a;
    --gold: #e8a921;
    --white: #ffffff;
    --ink: #1b3549;
    --backdrop: #e9e9ea;
  }
  * { margin: 0; padding: 0; box-sizing: border-box; }
  html, body { width: 1200px; height: 1095px; overflow: hidden; }
  body {
    background: var(--backdrop);
    font-family: "Montserrat", sans-serif;
    position: relative;
  }
  .card {
    position: absolute;
    left: 250px;
    width: 700px;
    height: 400px;
    border-radius: 22px;
    box-shadow: 0 14px 34px rgba(0,0,0,0.18);
    overflow: hidden;
  }
  .card--back { top: 95px; background: var(--navy); }
  .card--front { top: 600px; background: var(--white); }

  .back-mark {
    position: absolute;
    right: -120px; top: -60px;
    width: 380px; height: 380px;
    border-radius: 50%;
    border: 26px solid var(--navy-soft);
  }
  .back-brand {
    position: absolute;
    inset: 0;
    display: flex; align-items: center; justify-content: center;
    gap: 22px;
  }
  .back-brand .dot {
    width: 70px; height: 70px; border-radius: 50%;
    border: 5px solid var(--white);
  }
  .back-brand .name {
    color: var(--white);
    font-weight: 500;
    font-size: 64px;
    letter-spacing: 2px;
    text-transform: uppercase;
  }

  .front-brand {
    position: absolute;
    left: 70px; top: 0; bottom: 0;
    width: 270px;
    display: flex; flex-direction: column; align-items: center; justify-content: center;
    gap: 16px;
  }
  .front-brand .dot {
    width: 130px; height: 130px; border-radius: 50%;
    border: 8px solid var(--navy);
  }
  .front-brand .name {
    color: var(--navy);
    font-weight: 600;
    font-size: 28px;
    letter-spacing: 2px;
    text-transform: uppercase;
  }

  .divider {
    position: absolute;
    left: 365px; top: 105px;
    width: 3px; height: 190px;
    background: linear-gradient(var(--navy) 0 20%, transparent 20% 24%, var(--gold) 24% 76%, transparent 76% 80%, var(--navy) 80% 100%);
  }
  .divider { background: none; }
  .divider span { position: absolute; left: 0; width: 2px; }
  .divider .seg-top { top: 0; height: 36px; background: var(--navy); }
  .divider .seg-mid { top: 46px; height: 100px; width: 3px; background: var(--gold); }
  .divider .seg-bot { top: 156px; height: 34px; background: var(--navy); }

  .details {
    position: absolute;
    left: 400px; top: 112px;
    color: var(--ink);
  }
  .details .person {
    color: var(--gold);
    font-weight: 500;
    font-size: 27px;
    letter-spacing: 1px;
    text-transform: uppercase;
    line-height: 1;
  }
  .details .role {
    font-size: 16px;
    letter-spacing: 2px;
    margin-top: 6px;
  }
  .contact { list-style: none; margin-top: 30px; }
  .contact li {
    display: flex; align-items: center; gap: 10px;
    font-size: 17px;
    letter-spacing: 0.5px;
    line-height: 1;
    margin-bottom: 12px;
  }
  .contact svg { width: 15px; height: 15px; flex: none; }
</style>
</head>
<body>

<section class="card card--back" aria-label="Card back">
  <div class="back-mark"></div>
  <div class="back-brand">
    <span class="dot"></span>
    <span class="name">Bramwell</span>
  </div>
</section>

<section class="card card--front" aria-label="Card front">
  <div class="front-brand">
    <span class="dot"></span>
    <span class="name">Bramwell</span>
  </div>

  <div class="divider"><span class="seg-top"></span><span class="seg-mid"></span><span class="seg-bot"></span></div>

  <div class="details">
    <p class="person">Owen Hale</p>
    <p class="role">Managing Director</p>
    <ul class="contact">
      <li>
        <svg viewBox="0 0 16 16" aria-hidden="true"><path fill="#e8a921" d="M3.5 1.5l2.3 2.8-1.4 1.6c.9 1.9 2.6 3.6 4.5 4.5l1.6-1.4 2.8 2.3-1.5 2.2C7.2 13 3 8.8 1.5 3z"/></svg>
        +61 400 555 018
      </li>
      <li>
        <svg viewBox="0 0 16 16" aria-hidden="true"><rect x="1" y="3" width="14" height="10" rx="1" fill="#e8a921"/><path d="M1.5 3.8L8 9l6.5-5.2" fill="none" stroke="#fff" stroke-width="1.3"/></svg>
        info@bramwellllc.com
      </li>
      <li>
        <svg viewBox="0 0 16 16" aria-hidden="true"><g fill="none" stroke="#e8a921" stroke-width="1.4"><circle cx="8" cy="8" r="6.5"/><ellipse cx="8" cy="8" rx="3" ry="6.5"/><path d="M1.5 8h13"/></g></svg>
        www.bramwellllc.com
      </li>
    </ul>
  </div>
</section>

</body>
</html>
```